VENTURE CAPITAL GROUP BUSINESS CARD DESIGN

Venture Capital Group based in SF looking for a bold business card design. No trendy colour explosion, 3D effects etc. Just "simple" optical effects. Works on your brain, keeps your eye focused and sticks to your mind.
Target Market(s)
Technology startups
Industry/Entity Type
Venture Capital
Contact Information for Business Card
BARTHOLOMEW ELLING
MANAGING PARTNER
817 FERN ST SAN FRANCISCO, CA 94111
415.555.0142 O
415.555.0187 F
415.555.0236 C
bart@quillbrookfunds.example

```html
<!DOCTYPE html>
<html lang="en">
<head>
<meta charset="utf-8">
<title>Quillbrook Capital Group – Business Card</title>
<link href="https://fonts.googleapis.com/css2?family=Arimo:wght@400;700&display=swap" rel="stylesheet">
<style>
  :root {
    --page-bg: #e9e6e0;
    --card-white: #ffffff;
    --card-shade: #eeeeee;
    --edge-light: #e2e2e2;
    --edge-dark: #b9b9b9;
    --green-deep: #0f4a1f;
    --green-main: #1e7a33;
    --green-bright: #2f9a45;
    --green-text: #1b6a2e;
    --text-dark: #3a3a3a;
    --text-grey: #8c8c8c;
  }
  * { box-sizing: border-box; margin: 0; padding: 0; }
  html, body {
    width: 1200px; height: 950px; overflow: hidden;
    background: var(--page-bg);
    font-family: "Arimo", Arial, sans-serif;
  }
  .canvas {
    position: relative; width: 1200px; height: 950px;
    display: flex; flex-direction: column; align-items: center; justify-content: center; gap: 50px;
  }
  .card {
    position: relative; width: 700px; height: 400px; overflow: hidden;
    box-shadow: 0 6px 18px rgba(0,0,0,.18);
  }

  /* Back side */
  .card-back {
    background: radial-gradient(ellipse at 48% 40%, var(--green-bright) 0%, var(--green-main) 40%, var(--green-deep) 100%);
    display: flex; align-items: center; justify-content: center;
  }
  .card-back .brand { flex-direction: column; gap: 18px; }
  .card-back .brand-dot { width: 96px; height: 96px; background: #f2f2f2; }
  .card-back .brand-name { color: #f4f4f4; font-size: 30px; }

  /* Front side */
  .card-front {
    background: linear-gradient(180deg, var(--card-white) 0%, var(--card-white) 60%, var(--card-shade) 100%);
  }
  .front-edge {
    position: absolute; left: 0; top: 0; bottom: 0; width: 42px;
    background: linear-gradient(90deg, var(--edge-dark) 0%, var(--edge-light) 55%, #f6f6f6 100%);
  }
  .brand { display: flex; align-items: center; }
  .brand-dot {
    display: block; width: 64px; height: 64px; border-radius: 50%;
    background: radial-gradient(circle at 40% 35%, #ffffff 0%, #d9d9d9 100%);
  }
  .brand-name {
    font-family: "Arimo", Arial, sans-serif; font-weight: 700;
    letter-spacing: 1px; text-transform: uppercase;
  }
  .card-front .brand {
    position: absolute; left: 70px; top: 34px;
    flex-direction: column; align-items: flex-start; gap: 12px;
  }
  .card-front .brand-dot { margin-left: 52px; }
  .card-front .brand-name { color: var(--green-text); font-size: 22px; }

  .contact {
    position: absolute; left: 70px; top: 168px;
    color: var(--text-dark); font-size: 18px; line-height: 22px;
    list-style: none;
  }
  .contact .address { margin-bottom: 2px; }
  .contact li { display: flex; align-items: center; gap: 8px; }
  .contact svg { width: 15px; height: 15px; fill: var(--green-text); flex: none; }

  .person {
    position: absolute; right: 60px; top: 290px; text-align: left;
  }
  .person-name { color: var(--green-text); font-weight: 700; font-size: 22px; }
  .person-role { color: var(--text-grey); font-size: 18px; margin-top: 4px; padding-left: 40px; }
</style>
</head>
<body>
<main class="canvas">

  <section class="card card-back" aria-label="Card back">
    <div class="brand">
      <span class="brand-dot"></span>
      <span class="brand-name">Quillbrook Capital Group</span>
    </div>
  </section>

  <section class="card card-front" aria-label="Card front">
    <div class="front-edge"></div>

    <div class="brand">
      <span class="brand-dot"></span>
      <span class="brand-name">Quillbrook Capital Group</span>
    </div>

    <ul class="contact">
      <li class="address">817 Fern St San Francisco<br>CA 94111</li>
      <li>
        <svg viewBox="0 0 16 16" aria-hidden="true"><path d="M1 5c0-2 3-3 7-3s7 1 7 3v1h-3V4.5C10.5 4 5.5 4 4 4.5V6H1z M3 8l2-2h6l2 2v6H3z"/></svg>
        415.555.0142
      </li>
      <li>
        <svg viewBox="0 0 16 16" aria-hidden="true"><path d="M4 1h8v14H4z M5.5 3v9h5V3z"/></svg>
        415.555.0236
      </li>
      <li>
        <svg viewBox="0 0 16 16" aria-hidden="true"><path d="M4 1h7v4H4z M1 6h14v8H1z M3 8v2h6V8z"/></svg>
        415.555.0187
      </li>
      <li>
        <svg viewBox="0 0 16 16" aria-hidden="true"><path d="M1 3h14v10H1z M2.5 4.5L8 9l5.5-4.5z" fill-rule="evenodd"/></svg>
        bart@quillbrookfunds.example
      </li>
    </ul>

    <div class="person">
      <p class="person-name">Bartholomew Elling</p>
      <p class="person-role">Managing Partner</p>
    </div>
  </section>

</main>
</body>
</html>
```